Voralynx - Web Design Project

I am looking for a 5 page design.
I would like it to be like the design of this site: www.quorvantel.com.
Which means it can be all one page effectively. With quick scroll tabs at the top.
I would like it to include parallax scrolling (The parallax effect uses multiple backgrounds which seem to move at different speeds to create a sensation of depth (creating a faux-3D effect)).
I have uploaded my logo. I would like this to be used in the site design.
I would like the site design to include 3D DNA creative.
Please note the PixHarbor photos attached do not belong to me they are purely to inspire creative ideas. However I would be more than happy to purchase these photos to use if the designer thought this would be beneficial.
Requirements
Must have
- parallax scrolling
DNA pictures (3D effect)
Please use site for reference: www.quorvantel.com
Use at least 1 of the logos in design...

```html
<!DOCTYPE html>
<html lang="en">
<head>
<meta charset="utf-8">
<title>Voralynx – Hybrid Advertising</title>
<link href="https://fonts.googleapis.com/css2?family=Quicksand:wght@400;500;700&display=swap" rel="stylesheet">
<style>
:root{
  --ink:#2a2a2a;
  --brand:#3a3f9a;
  --white:#ffffff;
  --dna-deep:#12216e;
  --dna-mid:#3f63c9;
  --dna-light:#c9d6f2;
  --panel-dark:rgba(40,40,40,.82);
  --panel-light:rgba(235,235,235,.92);
  --media-bg:#303030;
  --stone:#9a9a9a;
}
*{margin:0;padding:0;box-sizing:border-box}
html,body{width:1200px;height:4027px;overflow:hidden}
body{font-family:"Quicksand",sans-serif;color:var(--ink);background:var(--white);position:relative}
.section{position:absolute;left:0;width:1200px;overflow:hidden}
.art{position:absolute}
p{font-size:17px;line-height:1.35}
.lead{font-size:24px;font-weight:500;margin-bottom:10px}
.section-title{font-weight:700;font-size:84px;line-height:1;letter-spacing:-1px}

/* hero */
.hero{top:0;height:786px;background:var(--white);box-shadow:0 10px 20px rgba(0,0,0,.15);z-index:2}
.hero .dna{left:0;top:0;width:600px;height:786px;
  background:radial-gradient(ellipse at 40% 45%,var(--dna-mid) 0%,var(--dna-deep) 30%,var(--dna-light) 60%,var(--white) 85%)}
.main-nav{position:absolute;top:38px;left:600px;display:flex;gap:34px}
.main-nav a{color:var(--brand);text-decoration:none;font-size:19px;font-weight:500}
.brand{position:absolute;left:780px;top:220px;width:280px;text-align:center}
.brand-mark{display:inline-block;width:56px;height:56px;border-radius:50%;background:var(--brand);margin-bottom:18px}
.brand-name{font-size:44px;font-weight:700;color:var(--brand);letter-spacing:6px}
.brand-tag{font-size:14px;color:var(--brand);letter-spacing:3px}
.hero-copy{position:absolute;left:617px;top:440px;width:480px}

/* about */
.about{top:846px;height:806px;background:var(--white)}
.about .molecule{left:800px;top:20px;width:400px;height:580px;
  background:radial-gradient(ellipse at 55% 50%,var(--dna-mid) 0%,#8fb1ec 35%,var(--white) 72%)}
.about-copy{position:absolute;left:150px;top:170px;width:500px}
.about .section-title{color:var(--brand);margin-bottom:20px}

/* services */
.services{top:1652px;height:786px;background:var(--white)}
.services .dna-left{left:0;top:0;width:440px;height:786px;
  background:radial-gradient(ellipse at 30% 40%,var(--dna-deep) 0%,var(--dna-mid) 30%,var(--dna-light) 60%,var(--white) 85%)}
.services .dna-right{right:0;top:0;width:200px;height:786px;
  background:radial-gradient(ellipse at 80% 50%,var(--dna-mid) 0%,var(--dna-light) 50%,var(--white) 85%)}
.services .section-title{position:absolute;left:645px;top:172px;color:var(--ink)}
.services .panel{position:absolute;left:129px;top:242px;width:947px;height:423px;background:var(--panel-dark);color:var(--white);padding:34px 40px}

/* media */
.media{top:2438px;height:786px;background:var(--media-bg)}
.media .dna{left:0;top:0;width:520px;height:786px;opacity:.55;
  background:radial-gradient(ellipse at 30% 40%,var(--dna-mid) 0%,#1b2a5c 40%,var(--media-bg) 80%)}
.media .section-title{position:absolute;left:200px;top:190px;color:var(--white)}
.media .panel{position:absolute;left:200px;top:302px;width:920px;height:383px;background:var(--panel-light);padding:34px 40px}

/* contact */
.contact{top:3224px;height:803px;background:linear-gradient(160deg,#b8b8b8,var(--stone) 55%,#7c7c7c)}
.contact .sculpture{left:560px;top:60px;width:520px;height:260px;
  background:radial-gradient(ellipse at 50% 50%,#5fa9d8 0%,#2c5f95 40%,rgba(154,154,154,0) 75%)}
.contact .relief{left:0;top:560px;width:1200px;height:243px;
  background:linear-gradient(180deg,rgba(60,70,140,0) 0%,rgba(70,78,140,.45) 55%,rgba(60,60,90,.35) 100%)}
.contact .panel{position:absolute;left:160px;top:121px;width:505px;height:525px;background:var(--panel-dark);color:var(--white);padding:110px 40px 30px}
.contact .section-title{position:absolute;left:200px;top:150px;color:var(--ink);z-index:2}
.contact address{font-style:normal;font-size:18px;line-height:1.3;margin-bottom:24px}
.social{display:flex;gap:16px;margin-top:18px}
.social span{width:20px;height:20px;border-radius:50%;background:rgba(255,255,255,.75)}
</style>
</head>
<body>

<section class="section hero" id="home">
  <div class="art dna" role="img" aria-label="3D blue DNA double helix rendering"></div>
  <nav class="main-nav">
    <a href="#home">Home</a><a href="#about">About</a><a href="#services">Services</a><a href="#media">Media</a><a href="#contact">Contact</a>
  </nav>
  <div class="brand">
    <span class="brand-mark"></span>
    <div class="brand-name">VORALYNX</div>
    <div class="brand-tag">hybrid advertising</div>
  </div>
  <div class="hero-copy">
    <p class="lead">Building the future of mobile advertising.</p>
    <p>Voralynx have been working with audience targeting technologies since 2004. We are a collection of talented and experienced individuals from a variety of media and technology backgrounds.<br>Our infinity+ platform brings publishers, advertisers and our partners together in a way that has never been done before. Our proprietary technology and targeting layer allow brands to cut through the noise and directly hit on the impressions that reach the audiences that can change their business.</p>
  </div>
</section>

<section class="section about" id="about">
  <div class="art molecule" role="img" aria-label="3D blue molecule structure"></div>
  <div class="about-copy">
    <h2 class="section-title">about</h2>
    <p class="lead">Building the future of mobile advertising.</p>
    <p>Quorvantel have been working with audience targeting technologies since 2004. We are a collection of talented and experienced individuals from a variety of media and technology backgrounds.<br>Our infinity+ platform brings publishers, advertisers and our partners together in a way that has never been done before. Our proprietary technology and targeting layer allow brands to cut through the noise and directly hit on the impressions that reach the audiences that can change their business.</p>
  </div>
</section>

<section class="section services" id="services">
  <div class="art dna-left" role="img" aria-label="3D blue DNA helix, left side"></div>
  <div class="art dna-right" role="img" aria-label="3D blue DNA helix, right edge"></div>
  <div class="panel">
    <p class="lead">Building the future of mobile advertising.</p>
    <p>Quorvantel have been working with audience targeting technologies since 2004. We are a collection of talented and experienced individuals from a variety of media and technology backgrounds.<br>Our infinity+ platform brings publishers, advertisers and our partners together in a way that has never been done before. Our proprietary technology and targeting layer allow brands to cut through the noise and directly hit on the impressions that reach the audiences that can change their business.<br>Quorvantel have been working with audience targeting technologies since 2004. We are a collection of talented and experienced individuals from a variety of media and technology backgrounds.<br>Our infinity+ platform brings publishers, advertisers and our partners together in a way that has never been done before. Our proprietary technology and targeting layer allow brands to cut through the noise and directly hit on the impressions that reach the audiences that can change their business.</p>
  </div>
  <h2 class="section-title">services</h2>
</section>

<section class="section media" id="media">
  <div class="art dna" role="img" aria-label="Faint DNA helix on dark background"></div>
  <h2 class="section-title">media</h2>
  <div class="panel">
    <p class="lead">Building the future of mobile advertising.</p>
    <p>Quorvantel have been working with audience targeting technologies since 2004. We are a collection of talented and experienced individuals from a variety of media and technology backgrounds.<br>Our infinity+ platform brings publishers, advertisers and our partners together in a way that has never been done before. Our proprietary technology and targeting layer allow brands to cut through the noise and directly hit on the impressions that reach the audiences that can change their business.<br>Quorvantel have been working with audience targeting technologies since 2004. We are a collection of talented and experienced individuals from a variety of media and technology backgrounds.<br>Our infinity+ platform brings publishers, advertisers and our partners together in a way that has never been done before. Our proprietary technology and targeting layer allow brands to cut through the noise.</p>
  </div>
</section>

<section class="section contact" id="contact">
  <div class="art sculpture" role="img" aria-label="3D brand sculpture on stone surface"></div>
  <div class="art relief" role="img" aria-label="Brand name carved in stone relief"></div>
  <div class="panel">
    <address>Australian Office:<br>Level 6<br>14 Harlow Lane<br>Fernbrook, Sydney<br>NSW 2999<br>AUS</address>
    <address>info@voralynx.com<br>(02) 5550 1942</address>
    <div class="social"><span></span><span></span><span></span></div>
  </div>
  <h2 class="section-title">contact us</h2>
</section>

</body>
</html>
```